Business Card Design for a Personal Trainer

I need a business card design for my job as a personal trainer. It should have a unique, modern and exclusive design. On the front there should be only my logo with my name and my job. 0163/2918374 Tobias Kellinger Lindenfeldweg 14 80412 Munich Germany The most important contact information is the web adress. it can be bigger than the rest, but its not necessary. The card should be 8,5cmx5,5cm big. Font: Roboto. Colors: black, white, gray, 56c1ff.

```html
<!DOCTYPE html>
<html lang="de">
<head>
<meta charset="utf-8">
<title>Tobias Kellinger – Personal Trainer</title>
<link rel="stylesheet" href="https://fonts.googleapis.com/css2?family=Roboto:ital,wght@0,300;0,400;0,500;0,700;0,900;1,700;1,900&display=swap">
<style>
  :root {
    --page-bg: #d9d6d1;
    --card-dark: #1f1f1f;
    --card-light: #ffffff;
    --ink: #1c1c1c;
    --ink-soft: #3a3a3a;
    --gray-band: #b5b5b5;
    --photo-light: #e6e6e6;
    --photo-dark: #4a4a4a;
    --white: #ffffff;
  }
  * { box-sizing: border-box; margin: 0; padding: 0; }
  html, body {
    width: 1189px; height: 1200px; overflow: hidden;
    background: var(--page-bg);
    font-family: "Roboto", Arial, sans-serif;
  }
  .card {
    position: absolute;
    left: 218px;
    width: 752px; height: 486px;
    overflow: hidden;
    box-shadow: 0 6px 18px rgba(0,0,0,.25);
  }
  .card--front { top: 76px; background: var(--card-dark); color: var(--white); }
  .card--back  { top: 606px; background: var(--card-light); color: var(--ink); }

  /* front */
  .brand {
    position: absolute; left: 0; right: 0; top: 150px;
    display: flex; align-items: center; justify-content: center; gap: 14px;
  }
  .brand__square { width: 26px; height: 26px; background: var(--white); }
  .brand__name { font-weight: 700; font-size: 40px; letter-spacing: 6px; color: var(--white); }

  .identity { position: absolute; left: 0; right: 0; text-align: center; }
  .card--front .identity { top: 282px; }
  .identity__name { font-weight: 400; font-size: 39px; line-height: 1; letter-spacing: .5px; }
  .identity__role {
    display: flex; align-items: center; justify-content: center; gap: 6px;
    margin-top: 6px; font-size: 15px; letter-spacing: 4.5px; font-weight: 400;
  }
  .identity__role::before, .identity__role::after {
    content: ""; display: block; width: 56px; height: 1.5px; background: currentColor;
  }

  /* back */
  .portrait {
    position: absolute; left: 18px; top: 48px; width: 330px; height: 420px;
    background: radial-gradient(ellipse at 50% 70%, var(--photo-dark) 0%, #7a7a7a 55%, var(--photo-light) 100%);
  }
  .card--back .identity { left: 330px; right: 22px; top: 90px; }
  .card--back .identity__name { font-size: 38px; }
  .card--back .identity__role { font-size: 15px; margin-top: 4px; }
  .card--back .identity__role::before, .card--back .identity__role::after { width: 58px; }

  .contact { position: absolute; left: 380px; width: 276px; text-align: center; }
  .contact__label { font-weight: 700; font-style: italic; font-size: 16px; color: var(--ink); }
  .contact__value { font-size: 22px; color: var(--ink-soft); margin-top: 2px; }
  .contact--phone { top: 180px; }
  .contact--email { top: 260px; }
  .contact__divider {
    position: absolute; left: 396px; top: 247px; width: 250px; height: 2px;
    background: linear-gradient(90deg, transparent, var(--ink) 20%, var(--ink) 80%, transparent);
  }
  .website {
    position: absolute; left: 362px; width: 320px; top: 346px; text-align: center;
    font-weight: 900; font-style: italic; font-size: 21px; letter-spacing: 1.8px; color: var(--ink);
  }
  .swoosh { position: absolute; left: 0; bottom: 0; width: 752px; height: 486px; pointer-events: none; }
</style>
</head>
<body>
  <section class="card card--front">
    <div class="brand">
      <span class="brand__square"></span>
      <span class="brand__name">KELLINGER</span>
    </div>
    <div class="identity">
      <h1 class="identity__name">TOBIAS KELLINGER</h1>
      <p class="identity__role">PERSONAL TRAINER</p>
    </div>
  </section>

  <section class="card card--back">
    <div class="portrait" role="img" aria-label="Black and white portrait of the trainer with arms crossed"></div>
    <svg class="swoosh" viewBox="0 0 752 486" aria-hidden="true">
      <path d="M0 402 C 220 470, 480 430, 752 356 L752 486 L0 486 Z" fill="var(--gray-band)"/>
      <path d="M0 420 C 240 482, 500 440, 752 350 L752 486 L0 486 Z" fill="var(--card-light)"/>
      <path d="M0 432 C 260 492, 520 448, 752 348 L752 486 L0 486 Z" fill="var(--card-dark)"/>
    </svg>
    <div class="identity">
      <h2 class="identity__name">TOBIAS KELLINGER</h2>
      <p class="identity__role">PERSONAL TRAINER</p>
    </div>
    <div class="contact contact--phone">
      <p class="contact__label">Phone:</p>
      <p class="contact__value">0163/2918374</p>
    </div>
    <div class="contact__divider"></div>
    <div class="contact contact--email">
      <p class="contact__label">Email:</p>
      <p class="contact__value">info@kellingerfit.de</p>
    </div>
    <p class="website">www.KELLINGERFIT.de</p>
  </section>
</body>
</html>
```